2022 Copper Gull Classic poster

Event poster for the 35th annual sailboat race from Galveston to Port Aransas. [will upgrade to guaranteed once a couple of serious designs are submitted] Hosted by Brinehaven Yacht Club in Seabrook TX, organized by Tern Ridge Sailing Foundation, a charity supporting youth sailing and amateur sailboat racing. The poster art (or elements of it) will also be used for T shirts. This year's theme is "Marigold Evenings" in honor of 35 years of sponsorship by Corvello Rum. Past posters normally include a full moon (usually orange) and a sailboat or numerous sailing yachts 30 foot and up. This year we would like to add the Cuban party theme. About 1/4 of the poster space (usually at the bottom) will focus on event sponsors. Brinehaven Yacht Club or its burgee should be included but it is a minor element.

Target Market(s)

adult racing and cruising sailors and sailing yacht owners in the Gulf of Mexico vacinity who like to race overnight to a big party

Industry/Entity Type

adult sailboat distance offshore racing

Requirements
Must have
• 30' or larger sailboat(s), full moon (often orange but not absolute requirement), Copper Gull Classic® with the registered trade mark symbol, date (Oct 6-8, 2022), reference to Brinehaven Yacht Club either in text or by including the burgee with BYC and a seahorse... see uploaded options, [much of the must haves could be addressed by including the registered trademark logo with 2022 included, maybe as one element of an art nouveau style poster... see Love the feel uploaded example]
Nice to have
• see uploaded "love the feel of this" for one idea on how to incorporate dirent must haves with nice to haves; reference to 35 or 35th annual, Marigold Evenings Party feel, Rum reference or Corvello Rum reference (bat logo, liquor bottle with "Rum" or generic cocktail in the hand of a partier, tropical party influence (like salsa dancing couple or steel drum band)
Should not have
• reference to any brand of alcohol other than Corvello rum (no Martini glass, no beer stein)

```html
<!DOCTYPE html>
<html lang="en">
<head>
<meta charset="utf-8">
<title>Copper Gull Classic 2022 Poster</title>
<link rel="stylesheet" href="https://fonts.googleapis.com/css2?family=Alfa+Slab+One&family=Bevan&family=Oleo+Script:wght@700&family=Montserrat:wght@500;600;800&display=swap">
<style>
  :root {
    --canvas-bg: #ececec;
    --sky-blue: #2aa3df;
    --sky-deep: #1b86c8;
    --sea-blue: #1f8fd0;
    --navy: #1a3f95;
    --ink: #0f2236;
    --stripe-dark: #1d5aa8;
    --stripe-light: #7cc6ec;
    --paper: #ffffff;
    --sand: #efe6d2;
    --sand-deep: #dfd4bd;
    --rum-red: #a51f3b;
    --moon: #f0902a;
    --tab-grey: #8a8a8a;
  }
  * { box-sizing: border-box; margin: 0; padding: 0; }
  html, body { width: 1013px; height: 1200px; overflow: hidden; background: var(--canvas-bg); }

  .poster {
    position: absolute; left: 87px; top: 0; width: 838px; height: 1200px;
    background: repeating-linear-gradient(45deg, var(--stripe-dark) 0 6px, var(--stripe-light) 6px 12px);
  }
  .poster__sheet { position: absolute; inset: 10px; background: var(--paper); }

  .sky {
    position: absolute; left: 20px; top: 20px; width: 780px; height: 643px;
    background:
      linear-gradient(to bottom, rgba(0,0,0,0) 60%, var(--sea-blue) 75%, var(--sky-deep) 100%),
      radial-gradient(circle at 50% 45%, #5cc3ef 0%, var(--sky-blue) 55%, var(--sky-deep) 100%);
    overflow: hidden;
  }
  .edition {
    position: absolute; left: 0; right: 0; top: 28px; text-align: center;
    font-family: "Alfa Slab One", serif; font-size: 104px; line-height: 1; letter-spacing: -2px;
    color: var(--navy);
    text-shadow: 0 0 0 #fff, 3px 3px 0 #fff, -3px -3px 0 #fff, 3px -3px 0 #fff, -3px 3px 0 #fff, 0 0 14px #bfe6fb;
  }
  .title-line {
    position: absolute; font-family: "Bevan", serif; line-height: 1; color: #fff;
    -webkit-text-stroke: 3px var(--navy); paint-order: stroke fill;
    text-shadow: 4px 4px 0 #bfe3f6, 0 0 10px rgba(255,255,255,.6);
  }
  .title-line--one { left: 120px; width: 560px; top: 168px; font-size: 122px; text-align: center; letter-spacing: -2px; }
  .title-line--two { left: 360px; width: 330px; top: 283px; font-size: 130px; text-align: center; }
  .title-line--three { left: 132px; width: 560px; top: 483px; font-size: 112px; text-align: center; letter-spacing: -2px; }
  .title-line sup { font-family: "Montserrat", sans-serif; font-size: 26px; -webkit-text-stroke: 1px var(--navy); vertical-align: top; position: relative; top: 14px; }

  .ship-moon-art {
    position: absolute; left: 116px; top: 325px; width: 232px; height: 146px;
    background: linear-gradient(90deg, #f4f6f8 0%, #e6eef4 55%, var(--moon) 70%, #e9781e 100%);
    border-radius: 6px;
  }

  .party {
    position: absolute; left: 20px; top: 663px; width: 780px; height: 494px; background: var(--sand);
  }
  .party__art {
    position: absolute; left: 54px; top: 25px; width: 593px; height: 111px;
    background: linear-gradient(90deg, #4a4036, #a9463f 30%, #c9a877 60%, #5b3a2e 100%); opacity: .55;
    border-radius: 4px;
  }
  .sponsor-mark {
    position: absolute; left: 651px; top: 20px; width: 116px; text-align: center;
    font-family: "Montserrat", sans-serif; font-weight: 800; font-size: 15px; color: var(--rum-red); letter-spacing: 1px;
  }
  .sponsor-mark__dot { display: block; width: 70px; height: 70px; margin: 8px auto 10px; border-radius: 50%; background: var(--rum-red); }

  .theme {
    position: absolute; left: 0; right: 0; top: 140px; text-align: center;
    font-family: "Oleo Script", cursive; font-weight: 700; font-size: 80px; line-height: 1; color: var(--ink);
    -webkit-text-stroke: 6px var(--rum-red); paint-order: stroke fill;
  }
  .venue-band {
    position: absolute; left: 37px; top: 268px; width: 734px; height: 52px; background: var(--rum-red);
    border-radius: 3px 14px 3px 14px;
    display: flex; align-items: center; justify-content: space-between; padding: 0 26px 0 24px;
    font-family: "Montserrat", sans-serif; font-weight: 500; font-size: 24px; color: #fff; letter-spacing: .3px;
  }
  .venue-band__burgee { font-weight: 800; font-size: 20px; }
  .event-date {
    position: absolute; left: 0; right: 0; top: 328px; text-align: center;
    font-family: "Montserrat", sans-serif; font-weight: 800; font-size: 46px; color: var(--ink); letter-spacing: .5px;
  }
  .sponsor-zone {
    position: absolute; left: 0; right: 0; top: 379px; bottom: 0; background: var(--sand-deep);
  }
  .sponsor-zone__tab {
    position: absolute; left: 2px; top: 4px; width: 22px; height: 110px; background: var(--tab-grey);
    color: #eee; font-family: "Montserrat", sans-serif; font-weight: 600; font-size: 9px; letter-spacing: .5px;
    writing-mode: vertical-rl; transform: rotate(180deg); display: flex; align-items: center; justify-content: center;
  }
</style>
</head>
<body>
  <div class="poster">
    <div class="poster__sheet">
      <section class="sky">
        <div class="edition">35th annual</div>
        <div class="title-line title-line--one">COPPER</div>
        <div class="ship-moon-art" role="img" aria-label="Tall ship under full sail beside an orange full moon over the sea"></div>
        <div class="title-line title-line--two">GULL</div>
        <div class="title-line title-line--three">CLASSIC<sup>®</sup></div>
      </section>
      <section class="party">
        <div class="party__art" role="img" aria-label="Cuban party scene: jazz band, salsa dancers and guests at café tables under parasols"></div>
        <div class="sponsor-mark"><span class="sponsor-mark__dot"></span>CORVELLO</div>
        <div class="theme">Marigold Evenings</div>
        <div class="venue-band">
          <span>BRINEHAVEN YACHT CLUB</span>
          <span class="venue-band__burgee">BYC</span>
          <span>SEABROOK, TX</span>
        </div>
        <div class="event-date">OCTOBER 6th-8th, 2022</div>
        <div class="sponsor-zone">
          <div class="sponsor-zone__tab">SPONSOR LOGO</div>
        </div>
      </section>
    </div>
  </div>
</body>
</html>
```